Sehr professionelles Design, dass genau unseren Ansprüchen entsprach. Der Designer hat jeweils zügig auf unsere Kommentare und Anfragen reagiert. Wir sind mit dem Endergebnis mehr als zufrieden. Gerne wieder.
Zielgruppe
Der Kern unserer Arbeit liegt in der Finanz- und Versicherungsberatung.
Für unsere Schaufenster möchten wir jeweils Werbung für unsere Kredit- resp. Versicherungsdienstleistungen machen.
Unsere Zielgruppe sind Personen, welche für ihr persönliches Projekt einen Privatkredit benötigen oder einen Versicherungscheck machen möchten. Bei beiden sollen möglichst keine Personen unter 25 Jahren angesprochen werden, da insb. die Werbung für Krediten an diese Altersgruppe in der Schweiz untersagt ist.
Aufgabenstellung
-(130 cm x 207 cm und 71 cm x 207 cm)
-Schaufenster Gross nur für Kredite
-Schaufenster Klein Fokus auf Versicherungen und Steuererklärung
-Falls möglich mit Schriftart Futura PT (Bold, Book etc.)
-Für das grosse Schaufenster (Privatkredite, 130 cm x 207 cm) bitte folgende gesetzliche Verbote beachten:
1. Werbung darf nicht an unter 25 Jährige gerichtet sein.
2. Es darf kein Eindruck erweckt werden, dass die Kredite besonders rasch oder ohne Prüfung gegeben werden (z.B. Sofortkredite, Expresskredite, 24 h Kredite, Kredite ohne Vorprüfung, Kredite auch mit Betreibungen etc.).
3. Es dürfen nicht ökonomisch sinnlose Argumente verwendet werden (z.B. Kredit aufnehmen, um Steuerschuld zu begleichen oder allgemein um Schulden abzubauen. Hier vor allem den Begriff Sparkredit vermeiden).
4. Keine Werbung für kostspielige Freizeitaktivitäten oder Feste (Kreditwerbung für die Finanzierung von Hochzeiten, Ferien, Reisen etc.)
5. Keine Abbildung von Bargeld.
-Was wir für die Privatkredite sehen möchten:
1. Erwähnung dass bereits ab 4.9% gewährt wird (z.B. Zins bereits ab 4.9% o.ä.)
2. Kreditbeträge bis CHF 250'000.00 werden gewährt.
3. Erwähnen dass unsere Büros im 3. OG sind, mit der Bitte dass sie gerne vorbeikommen können
4. Kleine Aussparung für Namen des Unternehmens
5. Kleine Aussparung für QR Code
6. Dieser Satz muss auf dem Plakat noch lesbar sein 'Die Kreditvergabe ist verboten, falls sie zur Überschuldung führt (Art. 3 UWG).'
Für den Rest möchten wir euch gerne kreativen Freiraum geben. Das Plakat soll aber wie bereits erwähnt sich mehr an Erwachsene ab 26 Jahren richten.
-Für das kleine Schaufenster (Versicherungen und Steuererklärungen, 71 cm x 207 cm) haben wir noch folgende Infos für euch:
-Wir sind unabhängige Versicherungsberater, lizenziert durch die VELBO (Alpine Handelsordnungsbehörde) und Veltrin (veltrin.ch, Weiterbildungsregister für Versicherungsberater..

```html
<!DOCTYPE html>
<html lang="de">
<head>
<meta charset="utf-8">
<title>Privatdarlehen – Schaufenster</title>
<link rel="stylesheet" href="https://fonts.googleapis.com/css2?family=Jost:wght@400;500;600;700&display=swap">
<style>
  :root{
    --green:#75c09a;
    --green-soft:#d6eadf;
    --dark:#263238;
    --ink:#263238;
    --paper:#fdfdfd;
    --bg:#ebebeb;
    --muted:#9aa3a8;
  }
  *{box-sizing:border-box;margin:0;padding:0}
  html,body{width:1200px;height:1200px;overflow:hidden;background:var(--bg);font-family:"Jost",sans-serif;color:var(--ink)}
  .window{position:absolute;top:43px;height:1114px;background:var(--paper);overflow:hidden}
  .window--credit{left:45px;width:700px}
  .window--insurance{left:775px;width:382px}
  .band{position:absolute;left:0;width:100%}
  .band--green{background:var(--green)}
  .band--dark{background:var(--dark);color:#fff}
  .art{position:absolute}
  .art__blob{width:100%;height:100%;border-radius:48% 52% 44% 56% / 55% 50% 50% 45%;
    background:radial-gradient(ellipse at 50% 55%,var(--green-soft) 0%,#e6f2ec 60%,rgba(230,242,236,0) 75%)}
  .dots{list-style:none}
  .dots li{position:relative;padding-left:14px}
  .dots li::before{content:"";position:absolute;left:0;top:50%;width:5px;height:5px;margin-top:-3px;border-radius:50%;background:currentColor}
  .hero{top:29px;height:136px;text-align:center;padding-top:22px}
  .hero__title{font-size:52px;font-weight:500;line-height:1;letter-spacing:.5px}
  .hero__sub{font-size:29px;font-weight:400;line-height:1.2;margin-top:2px}
  .intro{top:384px;height:210px;padding:10px 30px 0 45px;font-size:16.8px;line-height:22.8px;font-weight:400}
  .offer{top:685px;height:106px;padding:9px 0 0 33px;font-size:21px;line-height:29px;font-weight:400}
  .offer .dots li{padding-left:11px}
  .offer .dots li::before{top:15px;margin-top:0;width:4px;height:4px}
  .offer strong{font-weight:700}
  .visit{position:absolute;left:45px;top:858px;font-size:27px;font-weight:500;line-height:1.3}
  .visit__floor{display:block;color:var(--green);font-size:36px;font-weight:700;text-align:center;width:355px;margin:2px 0}
  .brand{position:absolute;left:478px;top:858px;width:192px;font-size:25px;font-weight:700;color:var(--ink);text-align:center;letter-spacing:.3px}
  .qr-slot{position:absolute;left:534px;top:911px;width:81px;height:81px;border:1px solid #c9c9c9;background:#fff}
  .legal{top:1073px;height:41px;color:var(--muted);font-family:Arial,sans-serif;font-size:16.5px;line-height:41px;padding-left:37px}
  .head{text-align:center;font-weight:500;font-size:30px;line-height:62px}
  .head--top{top:0;height:63px}
  .head--tax{top:580px;height:62px}
  .about{top:71px;height:119px;padding:16px 20px 0 25px;font-size:12.4px;line-height:17.5px}
  .list{position:absolute;font-size:17px;line-height:24.8px}
  .list--prices{left:52px;top:411px;color:var(--ink)}
  .list .note{font-size:11px;line-height:24px;padding-left:14px}
  .list .note::before{content:none}
  .tax-box{top:654px;height:191px}
  .list--tax{left:52px;top:23px;line-height:24.6px}
</style>
</head>
<body>
  <section class="window window--credit">
    <header class="band band--green hero">
      <h1 class="hero__title">Privatdarlehen</h1>
      <p class="hero__sub">Persönlich. Sicher. Einfach.</p>
    </header>
    <div class="art" style="left:192px;top:171px;width:317px;height:187px" role="img" aria-label="Illustration: unterschriebener Vertrag, Handschlag zwischen zwei Personen und Glühbirne mit Pflanzen">
      <div class="art__blob"></div>
    </div>
    <div class="band band--dark intro">
      Ob Sie eine Finanzierung für Ihr Fahrzeug benötigen, Ihr Unternehmen gründen oder weitere Ideen in die Tat umsetzen möchten: Wir haben die richtige Lösung für Sie. Unsere Bedürfnisse und Lebenssituationen machen uns alle einzigartig. Darum ist eine auf Ihnen massgeschneiderte Lösung wichtig, damit Sie sich auf das Wichtige konzentrieren können. Durch unsere langjährige Zusammenarbeit mit den führenden Kreditanstalten der Schweiz und unserer Erfahrung können wir Sie in der Suche nach dem richtigen Partner für Ihren Privatkredit unterstützen und Ihnen ein Angebot unterbreiten, dass am besten zu Ihren Bedürfnissen passt.
    </div>
    <div class="band band--green offer">
      <ul class="dots">
        <li>Darlehen sind ab <strong>4,9%</strong> erhältlich</li>
        <li>Kreditbeträge bis CHF <strong>250'000.00</strong><br>werden gewährt</li>
      </ul>
    </div>
    <div class="art" style="left:378px;top:582px;width:314px;height:220px" role="img" aria-label="Illustration: erwachsenes Paar neben einer Bonitätsanzeige mit Dokumenten und Karte">
      <div class="art__blob" style="background:radial-gradient(ellipse at 55% 60%,#d6eadf 0%,#e3f1e9 55%,rgba(227,241,233,0) 74%)"></div>
    </div>
    <p class="visit">Unser Büro befindet sich im<span class="visit__floor">3. Stock.</span>Wir beraten Sie gerne über</p>
    <div class="brand">lumen beratung</div>
    <div class="qr-slot" aria-label="Platz für QR-Code"></div>
    <footer class="band band--dark legal">Die Kreditvergabe ist verboten, falls sie zur Überschuldung führt (Art. 3 UWG).</footer>
  </section>

  <section class="window window--insurance">
    <h2 class="band band--green head head--top">Versicherungen</h2>
    <div class="band band--dark about">
      Wir sind unabhängige Versicherungsberater, lizenziert durch die VELBO (Alpine Handelsordnungsbehörde) und Veltrin (veltrin.ch, Weiterbildungsregister für Versicherungsberater) und beraten unsere Kunden seit 1999 in Versicherungsangelegenheiten.
    </div>
    <div class="art" style="left:30px;top:215px;width:315px;height:171px" role="img" aria-label="Illustration: drei Personen in einer Beratung am Tisch mit Dokumenten und Laptop">
      <div class="art__blob"></div>
    </div>
    <ul class="list dots list--prices">
      <li>Rentner und Studenten: CHF 50.00</li>
      <li>Einzelverdiener: CHF 60.00</li>
      <li>Doppelverdiener: CHF 70.00</li>
      <li>Eigenheimbesitzer: CHF 140.00*</li>
      <li class="note">*Nur eine Immobilie</li>
      <li>Erledigung innert 10 Arbeitstagen</li>
    </ul>
    <h2 class="band band--green head head--tax">Steuererklärungen</h2>
    <div class="band band--dark tax-box">
      <ul class="list dots list--tax">
        <li>Krankenkasse</li>
        <li>Fahrzeugversicherung</li>
        <li>Hausratversicherung</li>
        <li>Privathaftpflicht</li>
        <li>Rechtsschutz</li>
        <li>3. Säule a und b.</li>
      </ul>
    </div>
    <div class="art" style="left:55px;top:858px;width:271px;height:224px" role="img" aria-label="Illustration: Person am Schreibtisch mit grossem Taschenrechner und Laptop">
      <div class="art__blob" style="border-radius:50%"></div>
    </div>
  </section>
</body>
</html>
```